Redesign website for Wine Warehouse and Logistics company

We are looking to redesign https://www.brindlefreight.com/ website.

19 minute video showing what needs to be done:
https://files.quorvex.com/file/d/7kQ2mZ9xTbLw4RcVn8HsYpJd3FgA1eU/view?usp=sharing

Quorvex Deck shown in the video:
https://slides.quorvex.com/presentation/d/4pXr8wLmTq2ZbVn7KcJh3FsDyGe9RuAo5NiWtMkPzQa/edit?usp=sharing

I am also offering a $100 bonus on top of the contest award.
Updates

Holidays in India so we did not get enough design entries or quality.

Industry/Entity Type

Logistics company that handles Wine for Wineries.

Number of Pages Required

3 page

Colors

Designer to choose colors to be used in the design.

Requirements
Must have
• Check the 19 minute video showing what needs to be done.

```html
<!DOCTYPE html>
<html lang="en">
<head>
<meta charset="utf-8">
<title>Brindle Freight – Fulfillment Built for Wineries</title>
<link href="https://fonts.googleapis.com/css2?family=Libre+Caslon+Text:wght@400;700&family=Poppins:wght@400;500;600&display=swap" rel="stylesheet">
<style>
:root{
  --navy:#0e3f78;
  --navy-deep:#0a2f5c;
  --sky:#1ea3dc;
  --ink:#1f2430;
  --muted:#555c66;
  --line:#9cc6e6;
  --white:#ffffff;
  --footer:#141a22;
}
*{box-sizing:border-box;margin:0;padding:0}
html,body{width:1200px;height:4396px;overflow:hidden}
body{font-family:"Poppins",sans-serif;color:var(--ink);background:var(--white)}
.page{position:relative;width:1200px;height:4396px;overflow:hidden}
.abs{position:absolute}
a{color:inherit;text-decoration:none}
.front{z-index:3}

/* top bar + nav */
.topbar{left:0;top:0;width:1200px;height:37px;background:linear-gradient(90deg,#0b4f8f,#1476b8)}
.topbar ul{position:absolute;right:60px;top:10px;display:flex;list-style:none;font-size:12px;color:#fff}
.topbar li+li::before{content:"|";margin:0 14px}
.nav{left:0;top:37px;width:1200px;height:65px;background:#fff;box-shadow:0 2px 6px rgba(0,0,0,.08);z-index:4}
.brand{display:flex;align-items:center;gap:8px;font-family:"Libre Caslon Text",serif;font-size:20px;color:var(--navy);font-weight:400;letter-spacing:.3px}
.brand .dot{width:30px;height:30px;border-radius:50%;background:var(--navy)}
.nav .brand{position:absolute;left:60px;top:17px}
.menu{position:absolute;left:271px;top:24px;display:flex;gap:22px;font-size:12.5px;color:#555;list-style:none}
.menu .on{color:var(--navy);font-weight:500}
.btn{display:inline-block;font-family:"Libre Caslon Text",serif;font-weight:700;font-size:14px;border-radius:20px;text-align:center;letter-spacing:.5px}
.nav .signup{position:absolute;left:946px;top:14px;width:88px;height:36px;line-height:36px;background:var(--navy);color:#fff}
.nav .login{position:absolute;left:1050px;top:14px;width:89px;height:36px;line-height:34px;border:2px solid var(--navy);color:var(--navy)}

/* hero */
.hero{left:0;top:102px;width:1200px;height:666px;background:radial-gradient(ellipse at 60% 30%,#6b4530 0%,#3a2418 45%,#1f130c 100%)}
.hero-product{left:800px;top:400px;width:400px;height:375px;border-radius:6px;background:linear-gradient(135deg,#e9b9a4 0%,#d9a779 45%,#cfd6de 100%);opacity:.85;z-index:1}
.hero h1{position:absolute;left:61px;top:190px;font-family:"Libre Caslon Text",serif;font-weight:700;font-size:68px;line-height:86px;color:#fff;z-index:3}
.hero h1 span{color:var(--sky)}
.hero p{position:absolute;left:61px;top:368px;width:520px;font-size:14px;line-height:22px;color:#fff;z-index:3}
.hero .learn{position:absolute;left:61px;top:436px;width:142px;height:36px;line-height:36px;background:var(--navy);color:#fff;font-size:13px;z-index:3}
.hero .join{position:absolute;left:224px;top:436px;width:112px;height:36px;line-height:33px;border:1.5px solid #fff;color:#fff;font-size:13px;z-index:3}
.hero-edge{left:0;top:690px;width:1200px;height:80px;z-index:2}

/* section titles */
.title{position:absolute;left:0;width:1200px;text-align:center;font-family:"Libre Caslon Text",serif;font-weight:400;font-size:40px;color:var(--navy);letter-spacing:.5px;z-index:3}

/* all in one */
.feature{position:absolute;display:flex;align-items:center;gap:14px;font-family:"Libre Caslon Text",serif;font-size:15px;line-height:26px;color:var(--ink);z-index:3}
.feature.right{flex-direction:row-reverse;text-align:right}
.badge{width:74px;height:78px;flex:none}
.allinone-visual{left:345px;top:930px;width:500px;height:393px;border-radius:8px;background:linear-gradient(135deg,#e8a15a 0%,#f2c08a 40%,#2a2f36 60%,#dfe4ea 100%);opacity:.9}

/* cloud software */
.cloud{left:0;top:1340px;width:1200px;height:760px}
.cloud-title{position:absolute;left:61px;top:1458px;font-family:"Libre Caslon Text",serif;font-size:40px;line-height:54px;color:#fff;font-weight:400;z-index:3}
.inv-card{left:60px;top:1567px;width:560px;height:184px;border-radius:8px;background:rgba(255,255,255,.12);z-index:2}
.soft-item{position:absolute;left:82px;display:flex;gap:14px;align-items:flex-start;color:#fff;z-index:3}
.ring{width:58px;height:58px;flex:none}
.soft-item h3{font-family:"Libre Caslon Text",serif;font-weight:700;font-size:16px;line-height:20px;margin-top:18px}
.soft-item p{font-size:11.5px;line-height:26px;width:440px;margin-top:4px;color:#e8eef6}
.person-visual{left:660px;top:1442px;width:540px;height:675px;border-radius:50% 50% 8px 8px / 30% 30% 8px 8px;background:linear-gradient(160deg,#b8cce4 0%,#dfe7f2 40%,#c98a3c 70%,#b38a5e 100%);opacity:.55;z-index:1}

/* networks */
.net-card{position:absolute;width:253px;background:#fff;border:1.5px dashed var(--line);box-shadow:0 0 0 8px #f3f7fb;display:flex;flex-direction:column;align-items:center;justify-content:center;text-align:center;font-family:"Libre Caslon Text",serif;font-weight:700;font-size:16px;line-height:26px;color:var(--ink);padding:0 10px}
.net-card svg{width:62px;height:62px;margin-bottom:8px}

/* call to action */
.cta{left:0;top:2720px;width:1200px;height:620px}
.cta-title{color:#fff}
.cta-item{position:absolute;width:285px;text-align:center;color:#fff;z-index:3}
.cta-item .pin{display:block;margin:0 auto 8px;width:68px;height:80px}
.cta-item h3{font-family:"Libre Caslon Text",serif;font-weight:700;font-size:17px}
.cta-item p{font-size:12px;margin-top:10px}
.cta-hi{left:457px;top:2953px;width:285px;height:154px;background:rgba(255,255,255,.22)}
.truck-visual{left:256px;top:3150px;width:751px;height:332px;border-radius:10px 40px 30px 10px;background:linear-gradient(180deg,#e4e4e4 0%,#d6d8dc 60%,#4a4d52 100%)}

/* testimonials */
.box-visual{left:875px;top:3560px;width:325px;height:300px;border-radius:6px;background:linear-gradient(135deg,#c99465 0%,#e8c39a 50%,#5a1420 100%);opacity:.85}
.glass-visual{left:0;top:3610px;width:110px;height:300px;background:linear-gradient(180deg,rgba(150,30,40,.25),rgba(255,255,255,0))}
.partner{position:absolute;border-radius:50%;background:#fff;border:2px solid #d9dee5}
.quote-mark{left:578px;top:3734px;width:42px;height:42px;border-radius:50%;background:var(--sky);color:#fff;font-family:"Libre Caslon Text",serif;font-size:36px;line-height:52px;text-align:center;z-index:3}
.quote{left:350px;top:3796px;width:500px;text-align:center;font-size:12px;line-height:19px;color:var(--muted);z-index:3}
.author{left:0;top:3878px;width:1200px;text-align:center;font-family:"Libre Caslon Text",serif;font-weight:700;font-size:17px;z-index:3}
.author-co{left:0;top:3903px;width:1200px;text-align:center;font-size:12px;color:var(--muted);z-index:3}

/* footer */
.footer{left:0;top:3920px;width:1200px;height:442px;background:linear-gradient(180deg,#1b232e 0%,#0f141b 100%)}
.footer .brand{position:absolute;left:60px;top:150px;color:#fff}
.footer .brand .dot{background:#fff}
.fcol{position:absolute;top:136px;color:#fff;font-size:12px}
.fcol h4{font-family:"Libre Caslon Text",serif;font-weight:700;font-size:17px;color:var(--sky);margin-bottom:12px}
.fcol ul{list-style:none}
.fcol li{line-height:26px}
.frow{display:flex;gap:12px;align-items:flex-start;margin-bottom:22px;line-height:20px}
.frow svg{width:24px;height:24px;flex:none}
.copy{left:0;top:4362px;width:1200px;height:34px;background:#1a8fd0;color:#fff;font-size:12px;text-align:center;line-height:34px}
</style>
</head>
<body>
<div class="page">

  <div class="abs topbar">
    <ul><li>Contact Us</li><li>About Us</li><li>Blog</li><li>Our Network</li></ul>
  </div>

  <header class="abs nav">
    <div class="brand"><span class="dot"></span>Brindle Freight</div>
    <ul class="menu">
      <li class="on">Home</li><li>Wine Fulfillment</li><li>Wine Compliance</li><li>Why Brindle?</li><li>Software</li><li>Integrations</li><li>Services</li>
    </ul>
    <a class="btn signup">SIGN UP</a>
    <a class="btn login">LOG IN</a>
  </header>

  <section class="abs hero" role="img" aria-label="Wine cellar racks with bottles in warm low light">
    <h1>Fulfillment Built <span>for</span><br><span>Wineries</span></h1>
    <p>Tech-enabled 3PL that fulfills tasting room and eCommerce orders for direct-to-consumer wine fulfillment</p>
    <a class="btn learn">LEARN MORE</a>
    <a class="btn join">SIGN UP</a>
  </section>
  <div class="abs hero-product" role="img" aria-label="Rosé wine bottle, gift boxes and a laptop showing the inventory dashboard"></div>
  <svg class="abs hero-edge" viewBox="0 0 1200 80" preserveAspectRatio="none" aria-hidden="true">
    <path d="M0 60 C80 50 140 20 220 18 C300 16 340 40 420 48 C520 58 600 70 700 72 L1200 74 L1200 80 L0 80Z" fill="#fff"/>
  </svg>

  <h2 class="title" style="top:832px">ALL IN ONE SOLUTION</h2>
  <div class="abs allinone-visual" role="img" aria-label="Shipping boxes, barcode scanner, monitor with software and a wine gift box"></div>

  <svg width="0" height="0" style="position:absolute">
    <defs>
      <symbol id="shield" viewBox="0 0 74 78">
        <path d="M37 3 L70 14 L70 44 C70 60 55 72 37 76 C19 72 4 60 4 44 L4 14Z" fill="#fff" stroke="#0e3f78" stroke-width="2.5"/>
        <circle cx="37" cy="38" r="22" fill="none" stroke="#0e3f78" stroke-width="1.5"/>
      </symbol>
      <symbol id="ring" viewBox="0 0 58 58"><circle cx="29" cy="29" r="27" fill="#fff" stroke="#9cc6e6" stroke-width="3"/><circle cx="29" cy="29" r="20" fill="none" stroke="#0e3f78" stroke-width="1"/></symbol>
      <symbol id="pin" viewBox="0 0 68 80"><path d="M34 2a32 32 0 0 1 32 32c0 20-20 30-32 44C22 64 2 54 2 34A32 32 0 0 1 34 2z" fill="#1ea3dc"/></symbol>
    </defs>
  </svg>

  <div class="feature" style="left:60px;top:934px"><svg class="badge"><use href="#shield"/><rect x="28" y="29" width="18" height="18" fill="none" stroke="#1ea3dc" stroke-width="2"/></svg><span>Warehouse management<br>software</span></div>
  <div class="feature" style="left:60px;top:1036px"><svg class="badge"><use href="#shield"/><path d="M24 42 h18 v-10 h6 l5 6 v4 h-29z" fill="none" stroke="#0e3f78" stroke-width="2"/><circle cx="30" cy="45" r="3" fill="#0e3f78"/><circle cx="47" cy="45" r="3" fill="#0e3f78"/></svg><span>3-Tier Shipping</span></div>
  <div class="feature" style="left:60px;top:1139px"><svg class="badge"><use href="#shield"/><circle cx="37" cy="38" r="12" fill="none" stroke="#0e3f78" stroke-width="2"/><path d="M25 38h24M37 26v24" stroke="#0e3f78" stroke-width="1.5"/></svg><span>International<br>Shipping</span></div>
  <div class="feature" style="left:60px;top:1241px"><svg class="badge"><use href="#shield"/><rect x="27" y="30" width="20" height="17" fill="none" stroke="#0e3f78" stroke-width="2"/><path d="M27 36h20" stroke="#0e3f78" stroke-width="1.5"/></svg><span>Custom Branded<br>Boxes</span></div>

  <div class="feature right" style="right:61px;top:934px"><svg class="badge"><use href="#shield"/><path d="M29 38 l6 6 l11 -12" fill="none" stroke="#1ea3dc" stroke-width="2.5"/></svg><span>State Compliance</span></div>
  <div class="feature right" style="right:61px;top:1036px"><svg class="badge"><use href="#shield"/><rect x="28" y="28" width="18" height="20" fill="none" stroke="#0e3f78" stroke-width="2"/><path d="M32 34h10M32 39h10M32 44h6" stroke="#0e3f78" stroke-width="1.5"/></svg><span>Inventory Management<br>and Reports</span></div>
  <div class="feature right" style="right:61px;top:1139px"><svg class="badge"><use href="#shield"/><circle cx="37" cy="34" r="6" fill="none" stroke="#0e3f78" stroke-width="2"/><path d="M29 48v-4M33 48v-6M37 48v-4M41 48v-6M45 48v-4" stroke="#1ea3dc" stroke-width="2"/></svg><span>Pick and Tack</span></div>
  <div class="feature right" style="right:61px;top:1241px"><svg class="badge"><use href="#shield"/><path d="M37 24v28M25 31l24 14M49 31l-24 14" stroke="#0e3f78" stroke-width="2"/></svg><span>Temperature Controlled<br>Shipping</span></div>

  <svg class="abs cloud" viewBox="0 0 1200 760" preserveAspectRatio="none" aria-hidden="true">
    <path d="M0 10 C300 60 900 60 1200 0 L1200 600 C1000 650 860 720 640 735 C400 750 160 700 0 630Z" fill="#0e3f78"/>
  </svg>
  <div class="abs person-visual" role="img" aria-label="Smiling businessman holding a tablet with inventory software above a wooden wine crate"></div>
  <h2 class="cloud-title">ALL-IN-ONE CLOUD<br>BASED SOFTWARE</h2>
  <div class="abs inv-card"></div>

  <div class="soft-item" style="top:1578px"><svg class="ring"><use href="#ring"/><rect x="19" y="20" width="20" height="17" fill="none" stroke="#0e3f78" stroke-width="1.8"/></svg>
    <div><h3 style="margin-top:8px">Inventory management</h3><p>With Brindle's inventory portal, you can kiss your cumbersome spreadsheets goodbye. Track inventory levels across multiple sales channels, identify your best selling SKUs, blacklist old SKUs, receive low stock alerts, and more. Brindle's inventory system will give you complete visibility and control of your inventory.</p></div></div>
  <div class="soft-item" style="top:1766px"><svg class="ring"><use href="#ring"/><rect x="21" y="18" width="16" height="22" fill="none" stroke="#0e3f78" stroke-width="1.8"/></svg><h3>Orders management</h3></div>
  <div class="soft-item" style="top:1848px"><svg class="ring"><use href="#ring"/><circle cx="29" cy="29" r="10" fill="none" stroke="#0e3f78" stroke-width="1.8"/></svg><h3>Shipping management</h3></div>
  <div class="soft-item" style="top:1938px"><svg class="ring"><use href="#ring"/><path d="M18 38v-12l11-7 11 7v12z" fill="none" stroke="#0e3f78" stroke-width="1.8"/></svg><h3>Warehouse management</h3></div>

  <h2 class="title" style="top:2180px">OUR NETWORKS</h2>
  <div class="net-card" style="left:150px;top:2262px;height:171px"><svg viewBox="0 0 62 62"><path d="M10 52h42M18 52V34h8v18M30 52V24h8v28M42 52V14h8v38" fill="none" stroke="#1ea3dc" stroke-width="2.5"/></svg>Gain Competitive<br>advantage</div>
  <div class="net-card" style="left:457px;top:2293px;height:170px"><svg viewBox="0 0 62 62"><circle cx="22" cy="22" r="7" fill="none" stroke="#0e3f78" stroke-width="2.5"/><circle cx="40" cy="22" r="7" fill="none" stroke="#0e3f78" stroke-width="2.5"/><path d="M10 50c0-10 6-16 12-16s12 6 12 16M28 50c0-10 6-16 12-16s12 6 12 16" fill="none" stroke="#1ea3dc" stroke-width="2.5"/></svg>Avoid Heat hold storage and<br>losing customers</div>
  <div class="net-card" style="left:765px;top:2262px;height:171px"><svg viewBox="0 0 62 62"><path d="M8 40h30V22H8zM38 28h9l7 8v4H38z" fill="none" stroke="#1ea3dc" stroke-width="2.5"/><circle cx="17" cy="44" r="4" fill="#0e3f78"/><circle cx="46" cy="44" r="4" fill="#0e3f78"/></svg>Trucks leave every 2 weeks for<br>inventory replacement</div>
  <div class="net-card" style="left:150px;top:2492px;height:171px"><svg viewBox="0 0 62 62"><rect x="10" y="22" width="42" height="24" fill="none" stroke="#1ea3dc" stroke-width="2.5"/><circle cx="31" cy="14" r="7" fill="none" stroke="#0e3f78" stroke-width="2.5"/><path d="M18 32h26M18 38h18" stroke="#0e3f78" stroke-width="2"/></svg>Refrigerated trucks for<br>temperature control</div>
  <div class="net-card" style="left:457px;top:2521px;height:176px"><svg viewBox="0 0 62 62"><rect x="10" y="10" width="42" height="42" fill="none" stroke="#1ea3dc" stroke-width="2.5"/><path d="M10 24h42M10 38h42M24 24v28" stroke="#0e3f78" stroke-width="2"/></svg>Online inventory system to<br>order from inventory from<br>both warehouses.</div>
  <div class="net-card" style="left:765px;top:2492px;height:171px"><svg viewBox="0 0 62 62"><path d="M8 26L31 10l23 16v28H8z" fill="none" stroke="#1ea3dc" stroke-width="2.5"/><rect x="20" y="32" width="22" height="22" fill="none" stroke="#0e3f78" stroke-width="2"/></svg>Put inventory closer to your<br>customers to faster fulfillment</div>

  <svg class="abs cta" viewBox="0 0 1200 620" preserveAspectRatio="none" role="img" aria-label="Dark blue wine shop shelves behind the call to action">
    <defs><linearGradient id="ctaBg" x1="0" y1="0" x2="0" y2="1"><stop offset="0" stop-color="#0f3f77"/><stop offset="1" stop-color="#1b3c64"/></linearGradient></defs>
    <path d="M0 0 C200 60 400 80 600 80 C800 80 1000 60 1200 0 L1200 350 C1050 460 900 560 640 590 C380 610 150 540 0 470Z" fill="url(#ctaBg)"/>
  </svg>
  <h2 class="title cta-title" style="top:2848px">CALL TO ACTION</h2>
  <div class="abs cta-hi"></div>
  <div class="cta-item" style="left:141px;top:2920px"><svg class="pin"><use href="#pin"/><path d="M25 22c2-2 5 4 4 6l-2 2c1 4 5 8 9 9l2-2c2-1 8 2 6 4l-3 3c-8 2-20-10-18-18z" fill="#fff"/></svg><h3>CAll</h3><p>707.555.0148</p></div>
  <div class="cta-item" style="left:457px;top:2920px"><svg class="pin"><use href="#pin"/><rect x="20" y="24" width="28" height="20" fill="none" stroke="#fff" stroke-width="2.5"/><path d="M20 24l14 11 14-11" fill="none" stroke="#fff" stroke-width="2.5"/></svg><h3>Email</h3><p>info@brindlefreight.com</p></div>
  <div class="cta-item" style="left:773px;top:2920px"><svg class="pin"><use href="#pin"/><path d="M18 30l16-10 16 10v16H18z" fill="none" stroke="#fff" stroke-width="2.5"/><rect x="27" y="34" width="14" height="12" fill="none" stroke="#fff" stroke-width="2"/></svg><h3>Schedual pickup</h3><p>12:00 pm for following day delivery.</p></div>
  <div class="abs truck-visual" role="img" aria-label="White box delivery truck seen from the side"></div>

  <div class="abs glass-visual" role="img" aria-label="Red wine pouring into a glass"></div>
  <div class="abs box-visual" role="img" aria-label="Red wine bottle resting in an open wooden gift box with straw"></div>
  <h2 class="title" style="top:3570px">TESTIMONIALS</h2>
  <div class="partner" style="left:466px;top:3649px;width:92px;height:92px"></div>
  <div class="partner" style="left:645px;top:3649px;width:92px;height:92px"></div>
  <div class="partner" style="left:536px;top:3632px;width:126px;height:126px;border-color:var(--navy)"></div>
  <div class="abs quote-mark">&#8220;</div>
  <p class="abs quote">"I have been using Brindle Freight for over 5 years and I have been extremely happy with their services. I have never had any issues with tracking or claims and everything is done online. They resolve issues within 24 hours and make sure that I am satisfied with the outcome."</p>
  <p class="abs author">- Dale Morrow</p>
  <p class="abs author-co">Halvern Winery</p>

  <footer class="abs footer" role="img" aria-label="Dark wine bottle shelves behind the footer">
    <svg style="position:absolute;left:0;top:0" width="1200" height="60" viewBox="0 0 1200 60" preserveAspectRatio="none" aria-hidden="true"><path d="M0 0H1200V18C1100 30 1000 20 900 34C800 46 700 28 600 36C500 44 400 30 300 40C200 48 100 34 0 42Z" fill="#fff"/></svg>
    <div class="brand"><span class="dot"></span>Brindle Freight</div>
    <div class="fcol" style="left:336px"><h4>Site Map</h4>
      <ul><li>- Home</li><li>- Wine Fulfillment</li><li>- Wine Compliance</li><li>- Software</li><li>- Integrations</li><li>- Services</li><li>- Testimonials</li><li>- Blog</li><li>- Contact Us</li></ul></div>
    <div class="fcol" style="left:613px"><h4>Site Map</h4>
      <div class="frow"><svg viewBox="0 0 24 24"><path d="M12 2a7 7 0 0 1 7 7c0 5-7 13-7 13S5 14 5 9a7 7 0 0 1 7-7z" fill="none" stroke="#1ea3dc" stroke-width="2"/><circle cx="12" cy="9" r="2.5" fill="#1ea3dc"/></svg><span>48 Cellar Lane, Valemont,<br>CA 95012</span></div>
      <div class="frow"><svg viewBox="0 0 24 24"><path d="M5 3c2-1 4 4 3 6l-2 1c1 3 4 6 7 7l1-2c2-1 7 1 6 3l-2 3C11 22 1 12 5 3z" fill="#1ea3dc"/></svg><span># (707) 555 0148</span></div>
      <div class="frow"><svg viewBox="0 0 24 24"><rect x="2" y="5" width="20" height="14" fill="none" stroke="#1ea3dc" stroke-width="2"/><path d="M2 5l10 8 10-8" fill="none" stroke="#1ea3dc" stroke-width="2"/></svg><span>support@brindlefreight.com</span></div>
    </div>
    <div class="fcol" style="left:889px"><h4>Hours of operation:</h4>
      <div class="frow"><svg viewBox="0 0 24 24"><circle cx="12" cy="12" r="9" fill="none" stroke="#1ea3dc" stroke-width="2"/><path d="M12 7v5l3 3" fill="none" stroke="#1ea3dc" stroke-width="2"/></svg><span>9:00–5:00 pm M-F<br>Saturday/Sunday: Closed<br><br>24 hour advance appointment<br>required.</span></div>
    </div>
  </footer>
  <div class="abs copy">Copyright © 2021 , Brindle Freight. All rights reserved.</div>

</div>
</body>
</html>
```